Business Card Design Needed

Business car design required, logo will be supplied.

Brambleford Power Surveyors are looking to become the leading provider of energy performance certificates to estate agents, landlords and home owners in the Yorkshire region of the UK.

The business card must be double sided and professional looking. Estate agents receive hundreds of cards from contractors and our card must stand out.

I require a two sided business card that is clean, modern and created by a designer that can think outside of the box.

Brand colours can be supplied .

Please ask if you have any questions.

Target Market(s)

Estate agents, landlords and property owners

Industry/Entity Type

Property - estate agency - energy consultants

Contact Information for Business Card

Tomas Rendell - Energy Assessor - 07311642705 - www.BramblefordPSV.co.uk - info@bramblefordpsv.co.uk

Font styles to use
Serif
Sans Serif

Colors
00AB8E
00BBA5
67D7C9
C6EFE9
E9F9F6

Requirements
Must have
• Use the provided logo, clean, professional and stand out from the crowd
Nice to have
• Clever use of text, spacing and brand colours
Should not have
• Clip art

```html
<!DOCTYPE html>
<html lang="en">
<head>
<meta charset="utf-8">
<title>Brambleford Power Surveyors – Business Card</title>
<link rel="stylesheet" href="https://fonts.googleapis.com/css2?family=Arimo:wght@400;700&display=swap">
<style>
  :root {
    --stage: #4f4f4f;
    --brand-blue: #0066a1;
    --brand-lime: #c3d800;
    --card-light: #ecebec;
    --white: #ffffff;
    --shadow: rgba(0,0,0,0.55);
  }
  * { margin: 0; padding: 0; box-sizing: border-box; }
  html, body { width: 1075px; height: 1200px; overflow: hidden; }
  body {
    background: var(--stage);
    font-family: "Arimo", Arial, sans-serif;
    position: relative;
  }
  .card {
    position: absolute;
    width: 663px;
    height: 396px;
    overflow: hidden;
    box-shadow: 3px 3px 2px var(--shadow);
  }
  .card--front { left: 207px; top: 187px; background: var(--brand-blue); }
  .card--back  { left: 203px; top: 638px; background: var(--card-light); }

  .front-panel { position: absolute; inset: 0; width: 100%; height: 100%; }

  .person { position: absolute; left: 34px; top: 118px; }
  .person__name {
    color: var(--brand-lime);
    font-size: 25px;
    font-weight: 400;
    letter-spacing: 0.2px;
    line-height: 1;
  }
  .person__role {
    color: var(--white);
    font-size: 16px;
    margin-top: 4px;
    letter-spacing: 0.3px;
  }

  .contacts { position: absolute; left: 34px; top: 213px; list-style: none; }
  .contacts__item {
    display: flex;
    align-items: center;
    gap: 6px;
    color: var(--white);
    font-size: 18.5px;
    height: 24px;
  }
  .contacts__icon { width: 18px; height: 18px; flex: none; }

  .brand {
    position: absolute;
    left: 112px;
    top: 152px;
    display: flex;
    align-items: center;
    gap: 18px;
  }
  .brand__mark { width: 78px; height: 78px; flex: none; }
  .brand__rule { width: 1.5px; height: 78px; background: var(--brand-blue); }
  .brand__name {
    color: var(--brand-blue);
    font-size: 27px;
    font-weight: 400;
    letter-spacing: 0.5px;
    line-height: 1.15;
  }
</style>
</head>
<body>

  <section class="card card--front" aria-label="Card front">
    <svg class="front-panel" viewBox="0 0 663 396" aria-hidden="true">
      <polygon points="292,0 663,0 663,396 437,396" fill="var(--brand-lime)"/>
    </svg>

    <div class="person">
      <h1 class="person__name">TOMAS RENDELL</h1>
      <p class="person__role">ENERGY ASSESSOR</p>
    </div>

    <ul class="contacts">
      <li class="contacts__item">
        <svg class="contacts__icon" viewBox="0 0 24 24" aria-hidden="true">
          <path d="M6.6 10.8a15.1 15.1 0 0 0 6.6 6.6l2.2-2.2c.3-.3.7-.4 1-.2 1.1.4 2.3.6 3.6.6.6 0 1 .4 1 1V20c0 .6-.4 1-1 1A17 17 0 0 1 3 4c0-.6.4-1 1-1h3.5c.6 0 1 .4 1 1 0 1.3.2 2.5.6 3.6.1.3 0 .7-.2 1z" fill="var(--brand-lime)"/>
          <path d="M14 3a7 7 0 0 1 7 7M14 6.5a3.5 3.5 0 0 1 3.5 3.5" stroke="var(--brand-lime)" stroke-width="1.8" fill="none"/>
        </svg>
        <span>07311642705</span>
      </li>
      <li class="contacts__item">
        <svg class="contacts__icon" viewBox="0 0 24 24" aria-hidden="true">
          <rect x="2" y="6" width="20" height="13" fill="var(--brand-lime)"/>
          <path d="M2 6l10 7 10-7" stroke="var(--brand-blue)" stroke-width="1.5" fill="none"/>
        </svg>
        <span>info@bramblefordpsv.co.uk</span>
      </li>
      <li class="contacts__item">
        <svg class="contacts__icon" viewBox="0 0 24 24" aria-hidden="true">
          <g stroke="var(--brand-lime)" stroke-width="1.8" fill="none">
            <circle cx="12" cy="12" r="9"/>
            <ellipse cx="12" cy="12" rx="4" ry="9"/>
            <path d="M3 12h18M4.5 7.5h15M4.5 16.5h15"/>
          </g>
        </svg>
        <span>www.BramblefordPSV.co.uk</span>
      </li>
    </ul>
  </section>

  <section class="card card--back" aria-label="Card back">
    <div class="brand">
      <svg class="brand__mark" viewBox="0 0 78 78" aria-hidden="true">
        <circle cx="39" cy="39" r="34" fill="none" stroke="var(--brand-blue)" stroke-width="6"/>
      </svg>
      <span class="brand__rule"></span>
      <h2 class="brand__name">BRAMBLEFORD<br>POWER SURVEYORS</h2>
    </div>
  </section>

</body>
</html>
```